KSO Talent Growth one-page marketing flyer

Need a modern and stylized one-page marketing flyer for unit of new statewide human resources unit. The reason I am using pixel forum is because our organizations internal communication design standards are bland, boring, and graphic design skills on internal marketing team are limited. There are a handful of requirements we can't ignore in regards to design "look-and-feel", but I'm confident there is talent among the Pixel Forum community that can design something that is clean, modern, and engaging.

I have attached high resolution images, flyer copy, approved RGB colors, and can detail the non-negotiable requirements we must abide by per organization design standards.

Target Market(s)

HR Managers and Executives

Font styles to use
Other font styles liked:
• Helvetica, Alternative Gothic 2

Requirements
Must have
• Refer to the KSO Single Page Template document. This is the primary requirement we must adhere to now matter how the remiander of the flyer is designed. As shown on that template, the top of the front page MUST feature the Capital Night Monday (file name) image, cropped exactly as it apears o the template. The cropped image on the top of the front page must also include the text and magenta colored stripe as that specific color identifies our particular division. The only font types that can be used for the text in the top banner of other copy is Impact and Alternate Gothic No 3 D - no other font types are allowed. Finally, the Approved RGB Colors ( file name) attachment lists the approved RGB colors that can be used for design/copy purposes (*ex. copy can be a shade of gray vs, black).
• Design must be modern. Open to vector type graphic elements or live icons to represent Consulting, Learning Solutions (translation: training/workshops), Tools/Resources
• Size of one-page marketing flyer is 8 1/2 x 11. Copy and graphic design on front and back.

```html
<!DOCTYPE html>
<html lang="en">
<head>
<meta charset="utf-8">
<title>KSO Talent Growth</title>
<link href="https://fonts.googleapis.com/css2?family=Arimo:ital,wght@0,400;0,700;1,400&display=swap" rel="stylesheet">
<style>
  :root {
    --magenta: #9c1c86;
    --ink: #222226;
    --ink-soft: #3a3a3e;
    --white: #ffffff;
    --rule: #a04a8c;
    --sky-top: #3d4690;
    --sky-low: #5a62ab;
  }
  * { margin: 0; padding: 0; box-sizing: border-box; }
  html, body { width: 927px; height: 1200px; overflow: hidden; background: var(--white); }
  body { font-family: "Arimo", Helvetica, Arial, sans-serif; color: var(--ink); position: relative; }

  .hero {
    position: absolute; left: 0; top: 0; width: 927px; height: 296px;
    background:
      radial-gradient(ellipse 90px 150px at 470px 190px, rgba(190,165,125,0.75) 0%, rgba(150,130,120,0.35) 55%, rgba(90,98,171,0) 100%),
      radial-gradient(ellipse 420px 170px at 120px 300px, #1c2434 0%, #26304a 50%, rgba(38,48,74,0) 100%),
      linear-gradient(180deg, var(--sky-top) 0%, #4e58a5 50%, var(--sky-low) 100%);
  }
  .hero-title {
    position: absolute; left: 54px; top: 56px; color: var(--white);
    font-size: 27px; line-height: 33px; font-weight: 400; letter-spacing: -0.2px;
  }
  .hero-title strong { font-weight: 700; display: block; }

  .section-heading {
    position: absolute; left: 54px; color: var(--magenta);
    font-size: 17.6px; font-weight: 700;
  }

  .copy { position: absolute; font-size: 14.8px; line-height: 19.2px; color: var(--ink); }
  .copy p + p { margin-top: 2.4px; }
  .copy .line { display: block; text-align: justify; text-align-last: justify; }
  .copy .line.end { text-align-last: left; }
  .col-left { left: 54px; width: 387px; }
  .col-right { left: 463px; width: 409px; font-size: 14.4px; }

  .team-photo {
    position: absolute; left: 463px; top: 320px; width: 409px; height: 384px;
    background: linear-gradient(135deg, #e8edf0 0%, #d8dde1 50%, #c4b7aa 80%, #a59a90 100%);
  }

  .pillars { position: absolute; left: 54px; top: 885px; list-style: none; }
  .pillars li {
    position: relative; padding-left: 25px; font-size: 15.4px; line-height: 21.6px;
    color: var(--ink);
  }
  .pillars li::before {
    content: ""; position: absolute; left: 1px; top: 8px; width: 6px; height: 6px;
    border-radius: 50%; background: var(--magenta);
  }

  .quote {
    position: absolute; left: 463px; top: 887px; width: 420px;
    color: var(--magenta); font-style: italic; font-size: 16px; line-height: 20.5px;
  }
  .quote-author {
    position: absolute; left: 463px; top: 932px; font-size: 13px; font-weight: 700; color: var(--ink-soft);
  }

  .divider { position: absolute; left: 54px; top: 989px; width: 818px; height: 1px; background: var(--rule); }

  .service-strip { position: absolute; left: 53px; top: 998px; height: 146px; display: flex; }
  .service-tile { height: 146px; }
  .tile-coaching { width: 222px; background: radial-gradient(circle at 35% 60%, #6a6f73 0%, #3a3e42 55%, #222427 100%); }
  .tile-consulting { width: 161px; background: linear-gradient(160deg, #c9ccd0 0%, #9ea2a7 55%, #6f7277 100%); }
  .tile-feedback { width: 223px; background: linear-gradient(135deg, #f6f6f6 0%, #e9e9e9 100%); }
  .tile-communication { width: 213px; background: linear-gradient(180deg, #4583c9 0%, #6aa0d8 60%, #96bbe2 100%); }
</style>
</head>
<body>
  <header class="hero" role="img" aria-label="State capitol dome lit at dusk against a deep blue sky, with trees in the foreground"></header>
  <h1 class="hero-title">Department of<br>Administrative Services<strong>KSO Talent Growth</strong></h1>

  <h2 class="section-heading" style="top:321px;">Topics will include</h2>
  <div class="copy col-left" style="top:365px;">
    <p>
      <span class="line">KSO Talent Growth is a unit of the Enterprise</span>
      <span class="line">Talent Management Services team. We offer State of NL</span>
      <span class="line">agencies and entities forward thinking consulting and</span>
      <span class="line">learning solutions services – with a focus on management</span>
      <span class="line end">development.</span>
    </p>
    <p>
      <span class="line">Whether as a trusted advisor or hands-on coach, our</span>
      <span class="line">goal is to help our clients in whatever capacity can be</span>
      <span class="line">most useful and help them be successful. We have</span>
      <span class="line">over 30 years of experience in the public and private</span>
      <span class="line">sector helping clients solve problems and implement</span>
      <span class="line">modern solutions that deliver results. Our management</span>
      <span class="line">development consultants are certified PMCA, TDIR, LDN,</span>
      <span class="line end">and WPIS professionals.</span>
    </p>
    <p>
      <span class="line">We are flexible in how we work, but uncompromising</span>
      <span class="line">on delivering value. We meet our clients where they</span>
      <span class="line">are “today” regarding their individual management</span>
      <span class="line end">development needs and opportunities.</span>
    </p>
  </div>

  <div class="team-photo" role="img" aria-label="Team of colleagues gathered around a laptop in a bright office"></div>

  <h2 class="section-heading" style="top:721px;">What we do</h2>
  <div class="copy col-left" style="top:766px;">
    <p>
      <span class="line">Adapting to a rapidly changing world and future workforce</span>
      <span class="line">is a defining challenge for today’s State of NL leaders</span>
      <span class="line">and managers. We help our enterprise HR partners and</span>
      <span class="line">managers get “future-ready” and prepare for the modern</span>
      <span class="line end">workplace by helping them:</span>
    </p>
  </div>
  <ul class="pillars">
    <li>Build transformational leaders</li>
    <li>Create a coaching culture</li>
    <li>Drive employee engagement</li>
  </ul>

  <div class="copy col-right" style="top:728px;">
    <p>
      <span class="line">Along with our client consulting services, we provide learning</span>
      <span class="line">and development solutions that are relevant, experiential,</span>
      <span class="line">and collaborative. Unlike many “one-size-fits-all” programs,</span>
      <span class="line">we partner with our clients to customize solutions for their</span>
      <span class="line end">unique needs and situations.</span>
    </p>
    <p>
      <span class="line">We pride ourselves on being “experts without ego”</span>
      <span class="line end">consultants who are committed to our client’s success.</span>
    </p>
  </div>

  <p class="quote">“Effective management is all about managing<br>in the short term, while also preparing for the future…”</p>
  <p class="quote-author">Dale Whitford, KSO Management Consultant</p>

  <div class="divider"></div>

  <div class="service-strip">
    <div class="service-tile tile-coaching" role="img" aria-label="Compass dial with the word coaching"></div>
    <div class="service-tile tile-consulting" role="img" aria-label="Keyboard with a blue consultancy services key"></div>
    <div class="service-tile tile-feedback" role="img" aria-label="Feedback checklist with smiley faces and a red pen"></div>
    <div class="service-tile tile-communication" role="img" aria-label="Street signs reading effective communication against a blue sky"></div>
  </div>
</body>
</html>
```